Product label for specialty fertilizer for cannabis

Create a label with our brand name and product information. The name of the new product is “Vardel” and the name is also the logo. The color palate is white/platinium/silver/shimmery. The product makes the flowers dense and hard so we want the logo to look strong and masculine. The liquid inside the bottle is white Which is what vardel means in Spanish
Also need a font for all the product information. See pics for example and
Target Market(s)
Cannabis growers
Industry/Entity Type
Cannabis
Colors
Designer to choose colors to be used in the design.
Requirements
Must have
- Strong visual presence for retail environment. Clean but bold look.
Nice to have
- Would be nice to have similar to a Tivo Mara font
Should not have
- Do not put any cannabis or marijuana images anywhere on the label

```html
<!DOCTYPE html>
<html lang="en">
<head>
<meta charset="utf-8">
<title>Vardel – Product Label</title>
<link href="https://fonts.googleapis.com/css2?family=Poppins:wght@300;400;500;600;700&family=Open+Sans:wght@600&display=swap" rel="stylesheet">
<style>
  :root {
    --canvas: #d4d4d4;
    --label-bg: #ececec;
    --panel-border: #bdbdbd;
    --box-bg: #dcdcdc;
    --strip: #9c9c9c;
    --bar: #929292;
    --ink: #3a3a3a;
    --ink-soft: #4a4a4a;
    --white: #ffffff;
    --band-dark: #3f3f37;
    --band-mid: #7d7c68;
    --band-light: #a8a78f;
    --alert-red: #d9141a;
  }
  * { margin: 0; padding: 0; box-sizing: border-box; }
  html, body { width: 1195px; height: 1200px; overflow: hidden; }
  body {
    background: var(--canvas);
    font-family: "Poppins", sans-serif;
    color: var(--ink);
    position: relative;
  }
  .label {
    position: absolute;
    left: 40px; top: 47px;
    width: 1115px; height: 1106px;
    background: var(--label-bg);
  }
  .brand-band {
    position: absolute; left: 0; top: 0;
    width: 100%; height: 294px;
    background: radial-gradient(ellipse at 55% 45%, var(--band-light) 0%, var(--band-mid) 40%, var(--band-dark) 100%);
    display: flex; align-items: center; justify-content: center;
  }
  .brand-band__texture { position: absolute; inset: 0; }
  .brand-name {
    position: relative;
    font-family: "Poppins", sans-serif;
    font-weight: 700;
    font-size: 150px;
    letter-spacing: 4px;
    color: var(--white);
    line-height: 1;
  }
  .brand-strip {
    position: absolute; left: 0; top: 294px;
    width: 100%; height: 23px;
    background: var(--strip);
  }
  .info-panel {
    position: absolute; left: 8px; top: 317px;
    width: 1096px; height: 789px;
    border: 3px solid var(--panel-border);
    border-top: none;
  }
  .block { position: absolute; }
  .heading-box {
    left: 29px; top: 348px; width: 481px; height: 45px;
    background: var(--box-bg);
    font-size: 22px; font-weight: 500; color: var(--ink);
    padding-left: 21px; line-height: 45px;
  }
  .body-text {
    font-size: 19.4px; font-weight: 300; line-height: 30px;
    text-align: justify; hyphens: auto;
  }
  .body-text strong { font-family: "Open Sans", sans-serif; font-weight: 600; font-size: 19px; }
  .body-text .brand-word { font-weight: 500; }
  .directions { left: 29px; top: 412px; width: 481px; }
  .warning-box {
    left: 29px; top: 788px; width: 481px; height: 83px;
    border: 4px solid var(--panel-border);
    display: flex; align-items: center;
  }
  .warning-box svg { margin-left: 22px; flex: none; }
  .warning-box p {
    margin-left: 28px; font-size: 22px; font-weight: 500; line-height: 32px; color: var(--ink);
  }
  .section-title { font-size: 22px; font-weight: 500; line-height: 30px; color: var(--ink); }
  .short-text { font-size: 20.5px; font-weight: 300; line-height: 30px; }
  .short-text strong { font-family: "Open Sans", sans-serif; font-weight: 600; font-size: 19.5px; }
  .prevention { left: 29px; top: 908px; width: 500px; }
  .store { left: 29px; top: 1018px; width: 500px; }
  .about-box {
    left: 565px; top: 347px; width: 520px; height: 259px;
    background: var(--box-bg);
    padding: 22px 29px 0 23px;
  }
  .child-bar {
    left: 565px; top: 633px; width: 520px; height: 66px;
    background: var(--bar);
    display: flex; align-items: center;
    color: var(--white); font-size: 24px; font-weight: 400; letter-spacing: 0.3px;
  }
  .child-bar svg { margin: 0 14px 0 8px; flex: none; }
  .instructions { left: 569px; top: 750px; width: 516px; }
  .net-contents { left: 599px; top: 880px; width: 124px; text-align: center; }
  .net-contents__caption { font-size: 15px; font-weight: 400; color: var(--ink-soft); }
  .net-contents__disc {
    margin: 4px auto 0; width: 168px; height: 168px; margin-left: -22px;
    border-radius: 50%; background: var(--strip); color: var(--white);
    display: flex; flex-direction: column; align-items: center; justify-content: center;
  }
  .net-contents__num { font-size: 56px; font-weight: 600; line-height: 50px; }
  .net-contents__unit { font-size: 27px; font-weight: 600; line-height: 34px; }
  .address { left: 781px; top: 886px; width: 300px; }
  .address p { font-size: 21px; font-weight: 400; line-height: 32px; color: var(--ink-soft); }
  .address .email { margin-top: 8px; font-weight: 700; color: var(--ink); }
</style>
</head>
<body>
  <div class="label">
    <header class="brand-band">
      <div class="brand-band__texture" role="img" aria-label="Metallic dotted halftone texture band in dark olive and silver tones"></div>
      <h1 class="brand-name">Vardel</h1>
    </header>
    <div class="brand-strip"></div>
    <div class="info-panel"></div>

    <div class="block heading-box">DIRACTIONS FOR USE:</div>
    <p class="block body-text directions"><strong>SHAKE WELL BEFORE USE</strong> Lorem Ipsum is simply dummy text of the printing and typesetting industry. Lorem Ipsum has been the industry's standard dummy text ever since the 1500s, when an unknown printer took a galley of type and scrambled it to make a type specimen book. It has survived not only five centuries, but also the leap into electronic typesetting, remaining essentially unchanged. It was popularised in the 1960s with the release of Norvane sheets containing Lorem Ipsum passages, and more recently with desktop publishing software.</p>

    <div class="block warning-box">
      <svg width="64" height="56" viewBox="0 0 64 56" aria-hidden="true">
        <path d="M32 4 L60 52 L4 52 Z" fill="#fff" stroke="var(--alert-red)" stroke-width="5" stroke-linejoin="round"/>
        <rect x="29.5" y="19" width="5" height="19" rx="2" fill="#222"/>
        <circle cx="32" cy="44" r="3" fill="#222"/>
      </svg>
      <p>WARNING FOR ORNAMENTAL<br>PLANT USE ONLY</p>
    </div>

    <div class="block prevention">
      <h2 class="section-title">PREVENTION:</h2>
      <p class="short-text"><strong>SHAKE WELL BEFORE USE</strong> Lorem Ipsum is simply dummy text of the printing and typesetting</p>
    </div>
    <div class="block store">
      <h2 class="section-title">STORE:</h2>
      <p class="short-text">&nbsp;Lorem Ipsum is simply dummy text of the</p>
    </div>

    <div class="block about-box">
      <p class="body-text"><span class="brand-word">VARDEL</span> is a productLorem Ipsum is simply dummy text of the printing and typesetting industry. Lorem Ipsum has been the industry's standard dummy text ever since the 1500s, when an unknown printer took a galley of type and scrambled it to make a type specimen book.</p>
    </div>

    <div class="block child-bar">
      <svg width="54" height="54" viewBox="0 0 54 54" aria-hidden="true">
        <circle cx="27" cy="27" r="24" fill="#fff" stroke="var(--alert-red)" stroke-width="3"/>
        <circle cx="22" cy="15" r="4" fill="#222"/>
        <path d="M22 20 L22 34 M16 26 L28 24 M22 34 L18 42 M22 34 L26 42" stroke="#222" stroke-width="3.5" stroke-linecap="round" fill="none"/>
        <rect x="31" y="24" width="7" height="14" rx="1" fill="#222"/>
        <line x1="10" y1="10" x2="44" y2="44" stroke="var(--alert-red)" stroke-width="3"/>
      </svg>
      KEEP OUT OF REACH OF CHILDREN
    </div>

    <div class="block instructions">
      <h2 class="section-title">INSTRUCTIONS:</h2>
      <p class="short-text">is a productLorem Ipsum is simply dummy text of the printing and typesetting</p>
    </div>

    <div class="block net-contents">
      <p class="net-contents__caption">NET CONTENTS</p>
      <div class="net-contents__disc">
        <span class="net-contents__num">12</span>
        <span class="net-contents__unit">POUNDS</span>
      </div>
    </div>

    <div class="block address">
      <h2 class="section-title">ADDRESS:</h2>
      <p>Marlon Pruett</p>
      <p>418-3306 Orvale Rd.</p>
      <p>Dellford Ohio</p>
      <p class="email">vardelinfo@vardel.com</p>
    </div>
  </div>
</body>
</html>
```